AMAZING WEBSITE DESIGN NEEDED FOR MAID / CLEANING SERVICE

NOTE: This is Website Design Only - No coding required

Please submit your designs ASAP as we want to pick a winner and get started!

Hey,

We are looking for a new amazing website design for a maid or cleaning service.

They have a horrible website that we want turned into a masterpiece.

As you will see on their current site:

http://tidyhavenco.examplehost.net/

They have a lot of stuff, very disorganized, and need help.

Here is what we need:

Colors: Same as current site, Orange, Gray, Black

Menu: Horizontal with same Menu items

Need a spot for a video on the homepage

Want content to be structured in a great format that is easy to read.

Want to highlight commercial and residential on the website homepage.

Also want a spot for customer testimonials

We want the site clean, professional, fresh and modern.

Please help by matching the logo design.

I look forward to your designs!
Updates

Hi All! Really appreciate your efforts and designs. I will be meeting with our client on Monday and will then be able to provide feedback after our meeting. If you have other ideas, please submit them. The more I can show him the better! Thanks!

Target Market(s)

The target market is residential home owners as well as commercial businesses who need cleaning on a regular basis.

This company cleans homes and offices for individuals.

Industry/Entity Type

Residential

Font styles to use
Sans Serif

Requirements
Must have
• Must match logo colors
Must have spot for video
Must have a clean look
Must have a bold look
Nice to have
• Highly visual
Should not have
• clutter
messy design
hard to read

```html
<!DOCTYPE html>
<html lang="en">
<head>
<meta charset="utf-8">
<title>Tidy Haven – Quality Commercial &amp; Residential Cleaning</title>
<link rel="stylesheet" href="https://fonts.googleapis.com/css2?family=Source+Sans+3:wght@400;600;700&family=Open+Sans:ital,wght@0,400;0,600;1,400&display=swap">
<style>
:root{
  --orange:#f07522;
  --orange-light:#f7931e;
  --orange-dark:#e0661a;
  --gray-dark:#3d3d3d;
  --gray-text:#555;
  --gray-light:#ececec;
  --gray-line:#dcdcdc;
  --footer:#2b2b2b;
  --white:#fff;
  --hero-a:#cfe3f2;
  --hero-b:#9ec6e4;
}
*{box-sizing:border-box;margin:0;padding:0}
html,body{width:804px;height:1200px;overflow:hidden;background:var(--white)}
body{position:relative;font-family:"Open Sans",Arial,sans-serif;color:var(--gray-text)}
.abs{position:absolute}

/* header */
.brand{left:58px;top:58px;display:flex;align-items:center;gap:8px}
.brand-mark{width:14px;height:14px;background:var(--orange)}
.brand-name{font-family:"Source Sans 3",Arial,sans-serif;font-weight:700;font-size:28px;color:var(--gray-dark);letter-spacing:-.3px}
.brand-tagline{left:92px;top:96px;font-family:"Open Sans",Arial,sans-serif;font-style:italic;font-weight:600;font-size:10px;color:var(--gray-text)}
.call{right:48px;top:24px;text-align:right;font-family:"Source Sans 3",Arial,sans-serif}
.call-label{font-size:14px;color:var(--gray-dark)}
.call-number{font-size:16px;color:var(--orange)}
.call-icon{right:26px;top:30px}
.search{left:570px;top:85px;width:175px;height:25px;border:1px solid #cfcfcf;font-size:11px;color:#666;padding:5px 9px}
.search svg{position:absolute;right:7px;top:6px}

/* navigation */
.nav{left:0;top:130px;width:804px;height:40px;background:linear-gradient(var(--orange-light),var(--orange-dark));display:flex;padding-left:58px}
.nav a{display:block;height:40px;line-height:40px;padding:0 17px;font-family:"Source Sans 3",Arial,sans-serif;font-weight:700;font-size:13px;color:var(--white);text-decoration:none;border-right:1px solid rgba(255,255,255,.25);text-shadow:0 1px 1px rgba(0,0,0,.25)}
.nav a.active{background:#5c5c5c;padding:0 20px}

/* hero */
.hero{left:0;top:170px;width:804px;height:298px;background:linear-gradient(100deg,var(--hero-a) 0%,#e8dcd2 45%,var(--hero-b) 100%)}
.hero-kicker{left:65px;top:274px;font-family:"Source Sans 3",Arial,sans-serif;font-size:22px;color:var(--gray-dark)}
.hero-title{left:64px;top:306px;font-family:"Source Sans 3",Arial,sans-serif;font-weight:700;font-size:44px;color:var(--gray-dark)}
.dots{left:373px;top:446px;display:flex;gap:3px}
.dots span{width:11px;height:11px;border-radius:50%;background:#e9e9e9}
.dots span:first-child{background:#555}

/* services */
.service{top:510px;width:250px;text-align:center}
.service-icon{margin:0 auto;width:94px;height:94px;border-radius:50%;background:var(--orange);display:flex;align-items:center;justify-content:center;box-shadow:inset 0 0 0 3px rgba(255,255,255,.0)}
.service h3{margin-top:20px;font-family:"Source Sans 3",Arial,sans-serif;font-weight:400;font-size:20px;color:var(--orange)}
.service p{margin-top:7px;font-size:11px;line-height:16px;color:var(--gray-text)}

/* welcome */
.section-title{font-family:"Source Sans 3",Arial,sans-serif;font-size:22px;color:var(--orange)}
.video{left:58px;top:789px;width:214px;height:130px;background:linear-gradient(135deg,#8a8a8a,#c9c9c9 55%,#9a9a9a);box-shadow:0 2px 4px rgba(0,0,0,.3)}
.video-play{left:83px;top:36px;width:46px;height:46px;border-radius:50%;background:rgba(60,60,60,.75)}
.video-bar{left:0;bottom:0;width:214px;height:15px;background:#1d1d1d;font-size:7px;color:#ccc}
.intro-lead{left:290px;top:792px;width:234px;font-family:"Source Sans 3",Arial,sans-serif;font-size:13px;line-height:20px;color:var(--gray-dark)}
.intro-body{left:290px;top:835px;width:234px;font-size:10px;line-height:17px;color:var(--gray-text)}

/* testimonial */
.quote{left:550px;top:790px;width:195px;height:80px;background:#f1f1f1;padding:12px 12px 0 20px;font-style:italic;font-size:9.5px;line-height:15.5px;color:#666}
.quote-tail{left:683px;top:870px}
.avatar{left:571px;top:884px;width:32px;height:32px;border-radius:50%;background:linear-gradient(#d9b9a4,#8f5b45)}
.reviewer{left:636px;top:889px;font-size:9.5px;font-weight:600;color:var(--gray-dark);line-height:18px}

/* features band */
.band{left:0;top:981px;width:804px;height:137px;background:var(--gray-light)}
.feature{top:1005px}
.feature h4{font-family:"Source Sans 3",Arial,sans-serif;font-weight:400;font-size:19px;line-height:24px;color:var(--gray-dark)}
.feature p{margin-top:6px;font-size:10px;line-height:17px;color:var(--gray-text)}

/* footer */
.footer{left:0;top:1118px;width:804px;height:82px;background:var(--footer);font-family:Arial,sans-serif;font-size:10px;color:#eee}
.social{display:flex;gap:10px;position:absolute;right:66px;top:30px}
.social span{width:24px;height:24px}
</style>
</head>
<body>

<header>
  <div class="abs brand"><span class="brand-mark"></span><span class="brand-name">Tidy Haven</span></div>
  <div class="abs brand-tagline">Quality Commercial &amp; Residential Cleaning</div>

  <div class="abs call">
    <div class="call-label">Call today</div>
    <div class="call-number">+61 02 5550 1234</div>
  </div>
  <svg class="abs call-icon" width="20" height="28" viewBox="0 0 20 28"><path d="M4 2c-3 2-3 7 0 14s8 10 12 9l2-4-4-3-2 2c-2-1-4-4-5-7l2-2-2-5z" fill="var(--orange)"/></svg>

  <div class="abs search">Search..
    <svg width="12" height="12" viewBox="0 0 12 12"><circle cx="5" cy="5" r="3.5" fill="none" stroke="#999" stroke-width="1.5"/><path d="M7.5 7.5L11 11" stroke="#999" stroke-width="1.6"/></svg>
  </div>
</header>

<nav class="abs nav">
  <a class="active" href="#">HOME</a>
  <a href="#">SERVICES</a>
  <a href="#">OUR EMPLOYEES</a>
  <a href="#">SPECIAL OFFERS</a>
  <a href="#">ABOUT</a>
  <a href="#">CONTACT</a>
  <a href="#" style="border-right:0">REQUEST A BID</a>
</nav>

<section>
  <div class="abs hero" role="img" aria-label="Photo of a cleaner wiping a window with a blue cloth and spray bottle"></div>
  <div class="abs hero-kicker">DUS AUTM VEUM IRIURE DOOR</div>
  <div class="abs hero-title">CLAIS ESTIAM</div>
  <div class="abs dots"><span></span><span></span><span></span><span></span></div>
</section>

<section>
  <div class="abs service" style="left:28px">
    <div class="service-icon">
      <svg width="46" height="46" viewBox="0 0 46 46" fill="var(--white)"><circle cx="17" cy="8" r="5"/><rect x="12" y="15" width="10" height="16" rx="2"/><rect x="12" y="30" width="4" height="12"/><rect x="18" y="30" width="4" height="12"/><path d="M22 19l10 14" stroke="#fff" stroke-width="2.5"/><rect x="29" y="33" width="12" height="7" rx="3"/></svg>
    </div>
    <h3>COMMERCIAL</h3>
    <p>Lorem ipsum dolor sit amet<br>morbi ut elit utipsum tristiqueatesque<br>habitant morbi Aenean massa.</p>
  </div>
  <div class="abs service" style="left:277px">
    <div class="service-icon">
      <svg width="46" height="46" viewBox="0 0 46 46" fill="var(--white)"><path d="M30 4l4 3-10 16-4-3z"/><path d="M10 24h22l4 8H6z"/><rect x="6" y="33" width="30" height="6"/></svg>
    </div>
    <h3>RESIDENTIAL</h3>
    <p>Lorem ipsum dolor sit amet<br>morbi ut elit utipsum tristiqueatesque<br>habitant morbi Aenean massa.</p>
  </div>
  <div class="abs service" style="left:526px">
    <div class="service-icon">
      <svg width="46" height="46" viewBox="0 0 46 46"><rect x="10" y="8" width="22" height="26" rx="2" transform="rotate(-30 21 21)" fill="none" stroke="#fff" stroke-width="3"/><path d="M22 26l6-6 10 10-6 8-10-4z" fill="#fff"/></svg>
    </div>
    <h3>SPECIAL EVENTS</h3>
    <p>Lorem ipsum dolor sit amet<br>morbi ut elit utipsum tristiqueatesque<br>habitant morbi Aenean massa.</p>
  </div>
</section>

<section>
  <h2 class="abs section-title" style="left:58px;top:743px">Welcome to Our Website!!</h2>
  <div class="abs video" role="img" aria-label="Video still of a smiling cleaner holding a sponge and spray bottle">
    <div class="abs video-play">
      <svg width="46" height="46" viewBox="0 0 46 46"><path d="M18 13l14 10-14 10z" fill="#eee"/></svg>
    </div>
    <div class="abs video-bar">
      <svg width="214" height="15" viewBox="0 0 214 15"><path d="M5 4l5 3.5-5 3.5z" fill="#ddd"/><rect x="14" y="6" width="110" height="3" fill="#555"/><rect x="14" y="6" width="48" height="3" fill="#d9262b"/><text x="130" y="10" fill="#ccc" font-size="6" font-family="Arial">1:26 / 3:22</text><rect x="170" y="6" width="18" height="3" fill="#d9262b"/><text x="198" y="10" fill="#ccc" font-size="6" font-family="Arial" font-style="italic">HD</text></svg>
    </div>
  </div>
  <p class="abs intro-lead">Nlaritas est etiam processus dynamicus, qui seq uitur mutationem consuetudium.</p>
  <p class="abs intro-body">Claritas est etiam processus dyna micus, qui sequiturim utationem consuetudium lectorum. Mirum est notarenq uam littera gothica, quam nunc putamus parum claram, anteposuerit litterarum formas humanitatis per seacula quarta decima et quinta decima. Eodem modo typic.</p>

  <h2 class="abs section-title" style="left:552px;top:743px">Testimonials</h2>
  <blockquote class="abs quote">Fusce feugi malesuada odio. Morbinunc do gravida at, cursus nec, luctus lorem. Maicn as tristique orci acd sem Lorem sum. quam nunc putamus parum claram.</blockquote>
  <svg class="abs quote-tail" width="22" height="12" viewBox="0 0 22 12"><path d="M0 0h22L0 12z" fill="#f1f1f1"/></svg>
  <div class="abs avatar" role="img" aria-label="Portrait of the reviewer"></div>
  <div class="abs reviewer">Maecenintty interucoqt<br>
    <svg width="10" height="10" viewBox="0 0 10 10" style="vertical-align:-1px;margin-right:6px"><circle cx="5" cy="3" r="2.5" fill="#555"/><path d="M0 10c0-4 10-4 10 0z" fill="#555"/></svg>Dana Morrow</div>
</section>

<section>
  <div class="abs band"></div>
  <svg class="abs" style="left:60px;top:1006px" width="64" height="64" viewBox="0 0 64 64"><circle cx="32" cy="32" r="14" fill="none" stroke="#3c9a35" stroke-width="4"/><path d="M32 4l8 10H24zM6 48l6-12 6 12zM58 48l-6-12-6 12z" fill="#3c9a35"/></svg>
  <div class="abs feature" style="left:143px"><h4>Ecofriendly</h4><p>Tidy Haven is commit<br>ed to using Eco Green che<br>micals to keep your family<br>safe! No harsh</p></div>

  <svg class="abs" style="left:330px;top:1006px" width="40" height="64" viewBox="0 0 40 64"><path d="M20 4c-10 0-12 14 0 28L6 58l6 2 8-20 8 20 6-2-14-26c12-14 10-28 0-28zm0 8c5 0 5 8 0 14-5-6-5-14 0-14z" fill="#f59bb5"/></svg>
  <div class="abs feature" style="left:392px"><h4>Donations</h4><p>Tidy Haven is commit<br>ed to using Eco Green che<br>micals to keep your family<br>safe! No harsh</p></div>

  <svg class="abs" style="left:567px;top:1004px" width="50" height="64" viewBox="0 0 50 64"><path d="M14 36l-8 24 10-4 6 8 4-24zM36 36l8 24-10-4-6 8-4-24z" fill="var(--orange)"/><circle cx="25" cy="24" r="22" fill="var(--orange)"/><circle cx="25" cy="24" r="11" fill="none" stroke="#fff" stroke-width="3"/></svg>
  <div class="abs feature" style="left:637px"><h4>Satisfaction<br>Guaranteed!</h4><p>Tidy Haven is commit<br>ed to using Eco Green.</p></div>
</section>

<footer class="abs footer">
  <div class="abs" style="left:58px;top:25px">Terms and Conditions | Privacy Policy | Sitemap</div>
  <div class="abs" style="left:58px;top:49px">Copyrights © 2014. Privacy Policy</div>
  <div class="social" aria-label="Social links">
    <span style="background:#3b5b9c"></span>
    <span style="background:#2d9fd6"></span>
    <span style="background:#f07522"></span>
    <span style="background:#d9262b"></span>
  </div>
</footer>

</body>
</html>
```